Lets get creative with Pelloway Finance Brochure

I have used artfolkhub before for a previous brochure which is attached business BRAMLE Automotive. I would like to work together on a new project PELLOWAY Finance. https://pellowayfinance.com.au/
It is a boutique Finance company ideally targeting the small to Medium business s along with consumer finance. I have attached previous brochure to give an idea of layout. Once we have a layout i will send wording through.

Target Market(s)

business owners

Industry/Entity Type

Finance

Font styles to use
Serif

Colors
0355a3
fef3ec

```html
<!DOCTYPE html>
<html lang="en">
<head>
<meta charset="utf-8">
<title>Pelloway Finance – Trifold Brochure</title>
<link rel="stylesheet" href="https://fonts.googleapis.com/css2?family=Montserrat:wght@400;500;600;700&family=Open+Sans:wght@400&display=swap">
<style>
  :root {
    --brand-blue: #0355a3;
    --brand-navy: #1d2b5c;
    --paper: #ffffff;
    --backdrop: #e9eef2;
    --ink: #222631;
    --photo-dark: #2b2b2b;
    --photo-light: #bdbdbd;
    --heading-font: "Montserrat", sans-serif;
    --body-font: "Open Sans", sans-serif;
  }
  * { box-sizing: border-box; margin: 0; padding: 0; }
  html, body { width: 1200px; height: 900px; overflow: hidden; }
  body { background: var(--backdrop); position: relative; font-family: var(--body-font); color: var(--ink); }

  .brochure {
    position: absolute; left: 50px; top: 61px; width: 1100px; height: 778px;
    display: flex; background: var(--paper); box-shadow: 0 10px 30px rgba(0,0,0,.15);
  }
  .panel { position: relative; width: 366.67px; height: 100%; overflow: hidden; }

  /* Left panel */
  .panel-info { background: var(--paper); padding: 70px 38px 0 40px; }
  .section-heading {
    display: flex; align-items: center; gap: 14px;
    font-family: var(--heading-font); font-weight: 600; font-size: 17px;
    letter-spacing: 1px; color: var(--brand-blue); text-transform: uppercase; margin-bottom: 12px;
  }
  .heading-marker { width: 20px; height: 20px; background: var(--brand-blue); border-radius: 0 0 10px 0; flex: none; }
  .body-copy { font-size: 10.5px; line-height: 1.45; color: var(--ink); margin-bottom: 26px; padding-left: 34px; }
  .feature-image-wrap { position: relative; width: 262px; height: 186px; margin: 6px 0 0 34px; }
  .feature-image-frame {
    position: absolute; inset: -8px -8px 0 -8px; background: var(--brand-blue);
    border-radius: 0 0 120px 120px / 0 0 90px 90px;
  }
  .feature-image {
    position: absolute; inset: 0; border-radius: 0 0 120px 120px / 0 0 90px 90px;
    background: radial-gradient(circle at 45% 45%, #9a9aa2, #6f7a8a 55%, #b6b1aa);
  }
  .quote-block {
    position: absolute; left: 40px; right: 26px; bottom: 34px; height: 170px;
    border-left: 1.5px solid var(--brand-blue); border-bottom: 1.5px solid var(--brand-blue);
  }
  .quote-mark { position: absolute; font-family: var(--heading-font); font-weight: 700; font-size: 54px; color: var(--brand-blue); line-height: 1; }
  .quote-open { left: 16px; bottom: 18px; }
  .quote-close { right: 10px; top: 4px; }
  .quote-text {
    position: absolute; left: 58px; bottom: 30px; font-family: var(--heading-font);
    text-transform: uppercase; color: var(--ink); line-height: 1.15; letter-spacing: .5px;
  }
  .quote-text .small { font-size: 13px; font-weight: 500; }
  .quote-text .big { font-size: 20px; font-weight: 600; }

  /* Middle panel */
  .panel-contact { background: var(--brand-blue); color: #fff; }
  .contact-header {
    position: absolute; top: 0; left: 70px; width: 230px; height: 140px;
    background: var(--paper); border-radius: 0 0 90px 90px;
    display: flex; flex-direction: column; align-items: center; justify-content: center; gap: 10px;
  }
  .wordmark { font-family: var(--heading-font); font-weight: 600; color: var(--brand-navy); text-align: center; line-height: 1; }
  .wordmark-name { font-size: 22px; letter-spacing: 3px; }
  .wordmark-sub { font-size: 8px; letter-spacing: 9px; margin-top: 4px; padding-left: 9px; }
  .get-in-touch { font-family: var(--heading-font); font-weight: 600; font-size: 12px; letter-spacing: 1px; color: var(--brand-blue); text-transform: uppercase; }
  .info-heading { font-family: var(--heading-font); font-weight: 600; font-size: 13px; letter-spacing: 1px; text-transform: uppercase; text-align: center; }
  .info-line { font-size: 10.5px; text-align: center; line-height: 1.4; opacity: .95; }
  .hours { position: absolute; top: 168px; left: 0; right: 0; }
  .location-box { position: absolute; top: 230px; left: 30px; right: 30px; height: 250px; border: 1px solid rgba(255,255,255,.8); }
  .location-box .info-heading { position: absolute; top: -9px; left: 50%; transform: translateX(-50%); background: var(--brand-blue); padding: 0 12px; white-space: nowrap; }
  .location-box .info-line { margin-top: 16px; }
  .map-area { margin: 16px auto 0; width: 220px; height: 150px; background: linear-gradient(160deg, #2d70b3, #0b5eaa); border: 1px solid rgba(255,255,255,.35); }
  .contact-list { position: absolute; left: 40px; top: 560px; list-style: none; display: flex; flex-direction: column; gap: 14px; }
  .contact-item { display: flex; align-items: center; gap: 12px; font-size: 13px; }
  .contact-item.phone { font-family: var(--heading-font); font-weight: 600; font-size: 17px; letter-spacing: 1px; }
  .contact-icon { width: 22px; height: 22px; border-radius: 50%; background: #fff; display: flex; align-items: center; justify-content: center; flex: none; }

  /* Right panel */
  .panel-cover { background: var(--paper); }
  .cover-photo { position: absolute; top: 0; left: 0; right: 0; height: 430px; background: linear-gradient(135deg, var(--photo-dark) 0%, #555 55%, var(--photo-light) 100%); }
  .cover-wordmark { position: absolute; top: 555px; left: 0; right: 0; }
  .cover-wordmark .wordmark-name { font-size: 38px; letter-spacing: 5px; }
  .cover-wordmark .wordmark-sub { font-size: 12px; letter-spacing: 16px; margin-top: 8px; padding-left: 16px; }
</style>
</head>
<body>
  <main class="brochure">
    <section class="panel panel-info">
      <h2 class="section-heading"><span class="heading-marker"></span>About Us</h2>
      <p class="body-copy">Lorem ipsum dolor sit amet, consectetuer adipiscing elit, sed diam nonummy nibh euismod tincidunt ut laoreet dolore magna aliquam erat volutpat. Ut wisi enim ad minim veniam, quis nostrud. Lorem ipsum dolor sit amet, consectetuer adipiscing elit, sed diam nonummy nibh euismod tincidunt ut laoreet dolore magna aliquam erat volutpat. Ut wisi enim ad minim veniam, quis nostrud</p>
      <h2 class="section-heading"><span class="heading-marker"></span>Why Choose Us?</h2>
      <p class="body-copy">Lorem ipsum dolor sit amet, consectetuer adipiscing elit, sed diam nonummy nibh euismod tincidunt ut laoreet dolore magna aliquam erat volutpat. Ut wisi enim ad minim veniam, quis nostrud. Lorem ipsum dolor sit amet, consectetuer adipiscing elit, sed diam nonummy nibh euismod tincidunt ut laoreet dolore magna aliquam erat volutpat. Ut wisi enim ad minim veniam, quis nostrud</p>
      <div class="feature-image-wrap">
        <div class="feature-image-frame"></div>
        <div class="feature-image" role="img" aria-label="Photo of a solved colour puzzle cube on a desk with a soft blurred background"></div>
      </div>
      <div class="quote-block">
        <span class="quote-mark quote-open">&ldquo;</span>
        <p class="quote-text"><span class="small">Some </span><span class="big">Bold</span><br><span class="big">Statement </span><span class="small">Goes Here</span></p>
        <span class="quote-mark quote-close">&rdquo;</span>
      </div>
    </section>

    <section class="panel panel-contact">
      <header class="contact-header">
        <div class="wordmark">
          <div class="wordmark-name">PELLOWAY</div>
          <div class="wordmark-sub">FINANCE</div>
        </div>
        <div class="get-in-touch">Get In Touch</div>
      </header>
      <div class="hours">
        <h3 class="info-heading">Hours of Operation</h3>
        <p class="info-line">Mon - Fri: 8:30Am - 5:30Pm<br>Sat: 8:30Am - 12noon</p>
      </div>
      <div class="location-box">
        <h3 class="info-heading">Address</h3>
        <p class="info-line">14 Tarrant Lane<br>Ferndale, QLD, 4061</p>
        <div class="map-area" role="img" aria-label="Simple street map showing the office location"></div>
      </div>
      <ul class="contact-list">
        <li class="contact-item phone">
          <span class="contact-icon"><svg width="12" height="12" viewBox="0 0 24 24"><path fill="#0355a3" d="M6.6 10.8a15 15 0 0 0 6.6 6.6l2.2-2.2a1 1 0 0 1 1-.25 11.4 11.4 0 0 0 3.6.57 1 1 0 0 1 1 1V20a1 1 0 0 1-1 1A17 17 0 0 1 3 4a1 1 0 0 1 1-1h3.5a1 1 0 0 1 1 1c0 1.25.2 2.45.57 3.57a1 1 0 0 1-.25 1z"/></svg></span>
          07 3555 01 42
        </li>
        <li class="contact-item">
          <span class="contact-icon"><svg width="12" height="12" viewBox="0 0 24 24"><rect x="2" y="5" width="20" height="14" rx="2" fill="#0355a3"/><path d="M3 6l9 7 9-7" stroke="#fff" stroke-width="2" fill="none"/></svg></span>
          hello@pellowaymail.com
        </li>
        <li class="contact-item">
          <span class="contact-icon"><svg width="12" height="12" viewBox="0 0 24 24"><circle cx="12" cy="12" r="9" fill="none" stroke="#0355a3" stroke-width="2"/><path d="M3 12h18M12 3c3 3 3 15 0 18M12 3c-3 3-3 15 0 18" fill="none" stroke="#0355a3" stroke-width="1.6"/></svg></span>
          www.pellowayfinance.com.au
        </li>
      </ul>
    </section>

    <section class="panel panel-cover">
      <div class="cover-photo" role="img" aria-label="Black and white photo of two business people shaking hands over a desk"></div>
      <div class="wordmark cover-wordmark">
        <div class="wordmark-name">PELLOWAY</div>
        <div class="wordmark-sub">FINANCE</div>
      </div>
    </section>
  </main>
</body>
</html>
```